1300 Cratelofn Van wrap

We are forklift mechanics.
Design a simple wrap to suit our 4 vans with our logo.
Add some colour/design using the base colours happy to add other colours as suits and highlights/shadows to balance/break up the white but not over power it.
Include mobile number 0491 570 266

```html
<!DOCTYPE html>
<html lang="en">
<head>
<meta charset="utf-8">
<title>1300 Cratelofn – Van Wrap</title>
<link rel="stylesheet" href="https://fonts.googleapis.com/css2?family=Anton&family=Oswald:wght@600;700&display=swap">
<style>
  :root {
    --stage: #4a4a4a;
    --wrap-white: #ffffff;
    --brand-red: #c8161d;
    --brand-black: #141414;
    --panel-grey: #8a8d91;
    --art-grey: #a4a7ab;
    --text-white: #ffffff;
  }
  * { margin: 0; padding: 0; box-sizing: border-box; }
  html, body {
    width: 1200px; height: 682px; overflow: hidden;
    background: var(--stage);
  }
  .canvas { position: relative; width: 1200px; height: 682px; }
  .wrap-panel {
    position: absolute; left: 120px; top: 157px;
    width: 960px; height: 358px;
    background: var(--wrap-white);
    border-radius: 18px;
    overflow: hidden;
  }
  .wrap-shapes { position: absolute; inset: 0; width: 960px; height: 358px; }
  .forklift-art {
    position: absolute; left: 820px; top: 152px;
    width: 132px; height: 126px;
    background: linear-gradient(180deg, var(--art-grey), #979a9e);
    border-radius: 8px;
  }
  .company-mark {
    position: absolute; left: 685px; top: 49px;
    width: 60px; height: 60px;
    background: var(--text-white);
  }
  .company-name {
    position: absolute; left: 760px; top: 44px;
    font-family: "Oswald", sans-serif; font-weight: 600;
    font-size: 20px; line-height: 24px; letter-spacing: 0.5px;
    color: var(--text-white); text-transform: uppercase;
  }
  .brand-name {
    position: absolute; left: 306px; top: 160px;
    font-family: "Anton", sans-serif;
    font-size: 62px; line-height: 1;
    color: var(--brand-black); letter-spacing: 0;
    white-space: nowrap;
  }
  .services {
    position: absolute; left: 320px; top: 243px;
    font-family: "Oswald", sans-serif; font-weight: 700;
    font-size: 27px; line-height: 1;
    color: var(--brand-black); white-space: nowrap;
  }
  .phone {
    position: absolute; left: 394px; top: 286px;
    display: flex; align-items: center; gap: 8px;
    font-family: "Oswald", sans-serif; font-weight: 700;
    font-size: 33px; line-height: 1; color: var(--text-white);
  }
  .phone svg { width: 26px; height: 26px; }
</style>
</head>
<body>
  <main class="canvas">
    <section class="wrap-panel" aria-label="Van wrap side panel">
      <svg class="wrap-shapes" viewBox="0 0 960 358" aria-hidden="true">
        <!-- grey rear section -->
        <polygon points="938,0 960,0 960,358 772,358" fill="var(--panel-grey)"/>
        <!-- red diagonal header band -->
        <polygon points="708,0 938,0 872,138 620,138" fill="var(--brand-red)"/>
        <!-- black bar above brand name -->
        <rect x="481" y="147" width="300" height="10" fill="var(--brand-black)"/>
        <!-- red underline swoosh -->
        <polygon points="258,221 472,221 472,236 236,236" fill="var(--brand-red)"/>
        <polygon points="236,236 258,221 262,221 240,250 222,250" fill="var(--brand-red)"/>
        <!-- black phone band -->
        <polygon points="310,282 671,282 671,330 287,330" fill="var(--brand-black)"/>
        <!-- red lower band -->
        <polygon points="446,332 664,332 664,355 425,355" fill="var(--brand-red)"/>
      </svg>

      <div class="forklift-art" role="img" aria-label="Grey silhouette illustration of a forklift truck"></div>

      <div class="company-mark" aria-hidden="true"></div>
      <p class="company-name">Northgate<br>Lift<br>Service P/L</p>

      <h1 class="brand-name">1300 CRATELOFN</h1>

      <p class="services">HIRE - SALES - SERVICE - REPAIRS</p>

      <p class="phone">
        <svg viewBox="0 0 24 24" aria-hidden="true">
          <circle cx="12" cy="12" r="10.5" fill="none" stroke="#fff" stroke-width="2"/>
          <path d="M8.2 6.8c.5-.4 1.1-.3 1.4.2l1 1.7c.3.5.2 1-.2 1.4l-.7.6c.6 1.3 1.6 2.4 2.9 3l.6-.7c.4-.4.9-.5 1.4-.2l1.7 1c.5.3.6 1 .2 1.4l-.8.9c-.6.6-1.5.8-2.3.4-2.6-1.2-4.6-3.2-5.8-5.8-.4-.8-.2-1.7.4-2.3z" fill="#fff"/>
        </svg>
        0491 570 266
      </p>
    </section>
  </main>
</body>
</html>
```